Business card design needed with logo

My business is called QVM Solutions & it is targeted towards mobile equipment maintenance in the Mining and civil industry. My work involves maintenance planning and maintenance management plus also supply tradespeople on a labour hire basis. We can provide from basic shut-down machine rebuild plans to complete rebuild services supply plans and labour to anywhere in Australia. I would like to use the colours Black, Red and Grey, I had done a desgin as attached but doesn't really explain what we do and gears don't embroider well onto shirts.
Updates

I also wanted to see the something replace the gears maybe just making the QVM lettering look a bit different or put together differently 

Hello I have extended the deadline by a few extra days as I would like to update details on the front of card, details below & can be put which ever way looks good;

Neil Patton
Director
0417562938
QVM@mailbrook.com.au
www.qvmsolutions-demo.com.au

On the back of the card I would like to have the below printed;

Capable of providing, but not limited to, across Australia:
- Contract Maintenance Planning.
- Skilled Mobile Maintenance labour hire.
- New machine build specifications. 
- Plant risk assessments and inspections.
- Shut down and rebuild program planning.
- Preventative maintenance tasks, including build of materials lists, creation and review.

Target Market(s)

Contractors and companies that use small and large earthmoving and mining machines

Industry/Entity Type

Business

Contact Information for Business Card

Trading name is QVM Solutions
My name and title is
Neil Patton Director
0417 562 938
QVM@mailbrook.com.au

Logo Text

QVM

```html
<!DOCTYPE html>
<html lang="en">
<head>
<meta charset="utf-8">
<title>QVM Solutions – Business Card</title>
<link rel="stylesheet" href="https://fonts.googleapis.com/css2?family=Montserrat:wght@700;800&family=Mulish:wght@300&display=swap">
<style>
  :root {
    --backdrop: #8a8a8a;
    --card: #f7f7f5;
    --brand-red: #d40d17;
    --ink-dark: #3c3c3c;
    --ink-mid: #4a4a4a;
  }
  * { margin: 0; padding: 0; box-sizing: border-box; }
  html, body {
    width: 1200px;
    height: 1000px;
    overflow: hidden;
    background: var(--backdrop);
  }
  .stage {
    width: 1200px;
    height: 1000px;
    display: flex;
    align-items: center;
    justify-content: center;
  }
  .business-card {
    position: relative;
    width: 1000px;
    height: 612px;
    background: var(--card);
    box-shadow: 0 10px 30px rgba(0,0,0,0.25);
  }
  .brand-name {
    position: absolute;
    left: 110px;
    top: 190px;
    font-family: "Montserrat", sans-serif;
    font-weight: 800;
    color: var(--brand-red);
    font-size: 92px;
    line-height: 0.95;
    letter-spacing: -1px;
  }
  .brand-name .line { display: block; }
  .brand-name .line-small { font-size: 54px; letter-spacing: 0; margin-top: 8px; }
  .contact-block {
    position: absolute;
    right: 80px;
    top: 230px;
    text-align: right;
  }
  .person-name {
    font-family: "Montserrat", sans-serif;
    font-weight: 700;
    font-size: 50px;
    color: var(--ink-dark);
    letter-spacing: 1px;
  }
  .person-title {
    font-family: "Montserrat", sans-serif;
    font-weight: 700;
    font-size: 38px;
    color: var(--brand-red);
    margin-top: 2px;
    letter-spacing: 1px;
  }
  .contact-line {
    font-family: "Mulish", sans-serif;
    font-weight: 300;
    font-size: 34px;
    color: var(--ink-mid);
    line-height: 1.3;
    letter-spacing: 1px;
  }
  .contact-line.phone { margin-top: 24px; }
</style>
</head>
<body>
  <main class="stage">
    <section class="business-card">
      <div class="brand-name">
        <span class="line">QVM</span>
        <span class="line line-small">Solutions</span>
      </div>
      <div class="contact-block">
        <p class="person-name">Neil Patton</p>
        <p class="person-title">Director</p>
        <p class="contact-line phone">0417 562 938</p>
        <p class="contact-line email">QVM@mailbrook.com.au</p>
      </div>
    </section>
  </main>
</body>
</html>
```